Drift Us to Haven.co.nz .... Tourism business providing guided tours.

Design and build a website for our new company. The company is one where we take tourists to beautiful places for a fully guided tour for 2 weeks. Tours can follow our itinerary or be tailored to suit individual clients. .... Let us tell you a little of what we are about ....
Flying our clients to paradise for a ‘ Tailor Made ‘ tour or one where we organise everything and use our combined knowledge of more than 50 years experience in Indonesia where we travel to some of the places that are not well known on the tourist map, places that are often off the beaten track of tourists but that are spectacularly beautiful.
Our team .... Marcus Thornbury (Ex Iron Fern), Garrick Pellow, Sekar Pellow & Ratna Wulansari have reached a stage in life where making money is not essential but enjoying life is. We all have a passion to help others experience what we have when we travel to our paradise whether that is Indonesia, where we are starting our tours then we will be working on Thailand, Malaysia, Vietnam or New Zealand along with a number of other countries.
The experience of the ‘ Ladies ‘ in the team who are both native to the country along with my experience in the Film Production business where I have produced a number of documentaries on travelling through Indonesia and show casing the spectacular scenery there gives our clients access to what they will experience through my You Tube channel. …. https://www.vidstreamo.example/user/dpellowfilm/videos
We claim to be the only tour company that produces documentaries on what our guests can expect to experience on their travels with us. All trips are personally guided with one of our team and we can also Taylor make trips where groups can be personally guided by the Ex Iron Fern in our team Marcus Thornbury. Further to that we film and produce a Video of your trip as it happens ... that is something special that you get to keep and show friends & family.
To top that off we have Marcus Thornbury on board who can call on his experience of travelling with the Iron Fern team but also his position as entertainment director for the IF’S on tour.
Marcus also has a vast experience as a host where he has hosted celebrities and entertained large companies which included Corvane the French aircraft maker and Kestrel Digest in Bali.
He has also been involved with organising events and hosting guests for the Prince and Princess of Monaco.
Ratna has a Batchelor degree in marketing and management and worked in the hotel industry and also runs Lodgora villas where she is working on expanding that to the next level in Bali.
By chance we had been working on forming such a tour company individually and when we all realised this it was obvious we needed to form a company where we can call on our individual strengths.
The company will soon introduce other celebrity guides for our tours that will open opportunities for other ex players of International teams that are looking for opportunities when their playing careers finish.
What really stands out in Indonesia is the people - we consider they are the friendliest of all the countries we have travelled through. As a film maker I experience this throughout the country. When I intrude on peoples life and culture I am invariably met with a response that is so touching. The people of Indonesia are so proud of their way of life and equally as proud that I show such interest in their life. Our target market is clients that want to experience what we want to experience.
Bali is one part of our trip but the Island of Bali and the 17,200 other islands that make up the Indonesian Archipelago are what we have so much experience in travelling thru (some of - not all .... Yet?) and that is what makes our paradise the aim of the tours.
The company is currently being formed along with our Logo, brochures and a comprehensive website that will be online in a couple of weeks. Further to that and what in fact will be the main promotional tool for our company, we have a number of documentaries that will showcase ‘ Radiant Isles ‘ from the air and the ground that have been produced and are under production by our own in-house Film production company Greenharbour films.
Links :https://www.vidstreamo.example/watch?v=Qx7pLm2TzRa&feature=vs.be&ref=Kd93hTpWmz0eLqRvXcYbNa51GsUjHwPoIfEkZt&app=desktop
Our contact details :
‘ Drift us to Haven ‘ driftustohavennz@mailbay.example
Garrick & Sekar Pellow oakbarn_goods@netlink.example
Marcus Thornbury: mthornbury17@mailbay.example

Target Market(s)

Older people with money to spend on holidays in Paradise .... We are adamant, at this stage that we are looking at the higher end of the market so that our tours are unique and not a crowded tour where all follow the leader. We want to retain the flexibility so that at the start of each day we can offer alternatives to what is on the itinerary. For example some of the group could go rafting and the ladies may prefer to go in another direction and to facilitate this we will have more than one vehicle on hand to do this.

Industry/Entity Type

Tourism

Coding

Coded - Design and coding required

Number of Pages Required

5+ page

Font styles to use
Serif

Colors
0792cd
85cae6
00a990

Requirements
Must have
• Buttons so prospective clients can book and pay for a trip
• Links to various Documentaries we have on out You Tube Page .... Greenharbour Films
• Contact details for each of the partners
Nice to have
• A similar site to https://www.lotuspathjourneys.example/premium-tours/

```html
<!DOCTYPE html>
<html lang="en">
<head>
<meta charset="UTF-8">
<title>Drift Us to Haven</title>
<link rel="stylesheet" href="https://fonts.googleapis.com/css2?family=Lora:wght@400;700&family=Montserrat:wght@400;500;600&display=swap">
<style>
:root{
  --blue:#0792cd;
  --sky:#85cae6;
  --teal:#00a990;
  --ink:#1d1d1d;
  --text:#555;
  --grey-bg:#f1f1f1;
  --footer:#1f1f21;
  --white:#fff;
}
*{box-sizing:border-box;margin:0;padding:0}
html,body{width:1200px;height:3696px;overflow:hidden}
body{position:relative;background:var(--white);font-family:'Lora',Georgia,serif;color:var(--ink)}
.abs{position:absolute}

/* header */
.site-header{left:0;top:0;width:1200px;height:143px;background:var(--white)}
.brand{left:0;top:46px;width:1200px;text-align:center}
.brand-mark{display:inline-block;width:40px;height:40px;border-radius:50%;background:var(--blue);vertical-align:middle;margin-right:14px}
.brand-name{display:inline-block;vertical-align:middle;font-family:'Montserrat',sans-serif;font-weight:600;font-size:30px;color:var(--ink)}
.main-nav{left:0;top:143px;width:1200px;height:71px;background:var(--blue);display:flex;justify-content:center;align-items:center;gap:30px}
.main-nav a{color:var(--white);text-decoration:none;font-weight:700;font-size:14.5px;text-transform:uppercase;letter-spacing:.2px}

/* hero */
.hero{left:0;top:214px;width:1200px;height:513px;
  background:
    radial-gradient(ellipse 260px 120px at 830px 300px,rgba(120,220,210,.85),rgba(120,220,210,0) 70%),
    radial-gradient(ellipse 360px 200px at 1030px 160px,rgba(60,110,60,.95),rgba(60,110,60,0) 75%),
    radial-gradient(ellipse 380px 220px at 760px 470px,rgba(70,110,70,.9),rgba(70,110,70,0) 75%),
    linear-gradient(115deg,#0e2e5a 0%,#133f73 40%,#1d6a85 60%,#3a6d4a 80%,#2e5a3c 100%)}
.hero-card{left:113px;top:276px;width:498px;height:389px;background:var(--white);border:8px solid rgba(200,200,200,.8);padding:46px 38px}
.hero-kicker{font-size:18px;letter-spacing:.5px;color:var(--ink)}
.hero-title{font-size:31px;color:var(--blue);font-weight:400;margin-top:10px}
.hero-text{font-size:16px;line-height:28px;color:var(--text);margin-top:14px}
.hero-actions{display:flex;gap:15px;margin-top:20px}
.btn{display:inline-flex;align-items:center;justify-content:center;height:43px;font-family:'Lora',serif;font-weight:700;font-size:14px;text-transform:uppercase;text-decoration:none}
.btn-primary{background:var(--blue);color:var(--white);width:140px}
.btn-outline{border:1.5px solid #444;color:var(--ink);width:160px;font-weight:400}
.slider-dots{left:1137px;top:442px;display:flex;flex-direction:column;gap:10px}
.slider-dots span{width:12px;height:12px;border-radius:50%;background:var(--white)}
.slider-dots span:first-child{background:transparent;border:2px solid var(--white)}

/* about */
.about-frame{left:99px;top:830px;width:475px;height:395px;border:3px solid var(--blue)}
.about-photo{left:113px;top:845px;width:476px;height:399px;
  background:
    linear-gradient(180deg,#9fb3c0 0%,#7f9aa6 12%,rgba(0,0,0,0) 22%),
    radial-gradient(ellipse 160px 260px at 410px 300px,rgba(150,200,200,.8),rgba(150,200,200,0) 70%),
    linear-gradient(160deg,#2d4a2c 20%,#3b5f36 50%,#556b52 75%,#8aa7a4 100%)}
.about-copy{left:633px;top:862px;width:460px}
.eyebrow{font-family:'Montserrat',sans-serif;font-size:19px;color:var(--ink)}
.about-title{font-size:34px;font-weight:700;margin-top:8px}
.rule{width:69px;height:3px;background:var(--blue);margin-top:14px}
.about-text{font-size:14px;line-height:27.5px;color:var(--text);margin-top:14px}
.about-btn{margin-top:20px;width:160px;height:49px}

/* tours */
.band-grey{left:0;width:1200px;background:var(--grey-bg)}
.section-title{left:0;width:1200px;text-align:center;font-size:32px;font-weight:700;text-transform:uppercase}
.tour{overflow:hidden}
.tour-main{left:126px;top:1496px;width:463px;height:342px;
  background:
    radial-gradient(ellipse 200px 80px at 320px 120px,rgba(240,180,140,.6),rgba(240,180,140,0) 70%),
    linear-gradient(180deg,#566c94 0%,#8d8fa8 35%,#b39a94 50%,#4f5768 72%,#2d3442 100%);
  display:flex;align-items:center;justify-content:center}
.tour-label{color:var(--white);font-size:38px;font-weight:700;letter-spacing:1px}
.t1{left:596px;top:1496px;width:232px;height:165px;background:linear-gradient(180deg,#3f7fc6 0%,#8fb6d8 35%,#1fb9c2 70%,#19a6a8 100%)}
.t2{left:835px;top:1496px;width:232px;height:165px;background:linear-gradient(180deg,#4b4e6e 0%,#7c6d80 40%,#c6874a 75%,#6a4a36 100%)}
.t3{left:596px;top:1671px;width:232px;height:167px;background:linear-gradient(180deg,#a6bcd6 0%,#6f8bab 45%,#2f4862 75%,#b23a2a 88%,#2c3b4c 100%)}
.t4{left:835px;top:1671px;width:232px;height:167px;background:linear-gradient(180deg,#9cb5d3 0%,#b6b58f 40%,#7e8d45 70%,#c77f3d 100%)}
.carousel-dots{left:567px;top:1900px;display:flex;gap:15px}
.carousel-dots span{width:13px;height:13px;border-radius:50%;background:#aaa}
.carousel-dots span:first-child{background:var(--blue)}

/* documentaries */
.video{display:flex;align-items:center;justify-content:center}
.v1{left:118px;top:2210px;width:468px;height:311px;
  background:radial-gradient(ellipse 200px 160px at 320px 150px,rgba(140,120,110,.6),rgba(140,120,110,0) 70%),
  linear-gradient(135deg,#1e2833,#3d4d5d 50%,#202a35)}
.v2{left:609px;top:2210px;width:465px;height:311px;
  background:radial-gradient(ellipse 120px 200px at 230px 260px,rgba(170,170,160,.6),rgba(170,170,160,0) 70%),
  linear-gradient(160deg,#3e5232,#6c7e5e 50%,#3a4a30)}
.video-caption{text-align:center;font-size:24px;font-weight:700;text-transform:uppercase;line-height:34px}

/* experts */
.expert{width:240px;text-align:center}
.avatar{width:108px;height:108px;border-radius:50%;margin:0 auto;background:radial-gradient(circle at 50% 45%,#d8b49a 0%,#b8907a 45%,#5e463a 100%);border:3px solid var(--white)}
.expert-name{font-size:23px;font-weight:700;color:#555;margin-top:24px;white-space:nowrap}
.expert-card{left:609px;top:2915px;width:256px;height:291px;background:var(--white);box-shadow:0 6px 18px rgba(0,0,0,.12);overflow:hidden}
.expert-card svg{position:absolute;left:0;top:0}
.expert-card .avatar{position:absolute;left:74px;top:32px}
.expert-card .expert-name{position:absolute;left:0;top:160px;width:256px;color:var(--blue);margin:0;font-size:22px}
.expert-email{position:absolute;left:0;top:220px;width:256px;text-align:center;font-size:14px;color:#555}
.arrow-btn{width:54px;height:54px;border-radius:50%;background:var(--white);box-shadow:0 2px 8px rgba(0,0,0,.15);display:flex;align-items:center;justify-content:center}

/* footer */
.site-footer{left:0;top:3292px;width:1200px;height:404px;background:var(--footer);color:var(--white)}
.footer-brand{left:118px;top:3460px}
.footer-brand .brand-mark{width:34px;height:34px;margin-right:10px}
.footer-brand .brand-name{color:var(--white);font-size:26px}
.footer-heading{font-size:20px;font-weight:400;color:var(--white)}
.footer-text{font-family:'Montserrat',sans-serif;font-size:13px;line-height:23px;color:#ddd}
.field{width:268px;height:36px;border:2px solid var(--white);border-radius:18px;font-family:'Montserrat',sans-serif;font-size:11px;color:#ccc;padding:9px 18px}
.subscribe{width:138px;height:35px;border-radius:18px;background:var(--blue);color:var(--white);font-weight:700;font-size:13px;text-transform:uppercase;display:flex;align-items:center;justify-content:center}
.contact-row{display:flex;gap:16px;margin-bottom:14px}
.contact-row svg{flex:none;margin-top:4px}
.socials{left:510px;top:3595px;display:flex;gap:7px}
.socials span{width:40px;height:40px;border-radius:50%;border:2px solid var(--white)}
.copyright{left:0;top:3652px;width:1200px;text-align:center;font-size:14px;color:#eee}
</style>
</head>
<body>

<header class="abs site-header">
  <div class="abs brand"><span class="brand-mark"></span><span class="brand-name">Drift Us to Haven</span></div>
</header>
<nav class="abs main-nav">
  <a href="#">Destinations</a><a href="#">Tours</a><a href="#">Tailor-Made</a><a href="#">Special Offers</a><a href="#">About Us</a><a href="#">Before You Go</a><a href="#">Reviews</a><a href="#">Enquire Now</a>
</nav>

<section class="abs hero" role="img" aria-label="Aerial view of a tropical island coastline with turquoise shallows"></section>
<div class="abs hero-card">
  <p class="hero-kicker">WELCOME TO</p>
  <h1 class="hero-title">DRIFT US TO HAVEN</h1>
  <p class="hero-text">Nemo enim ipsam voluptatem quia voluptas sit aspernatur aut odit aut fugit, sed quia consequuntur magni dolores eos qui ratione voluptatem sequi nesciunt.</p>
  <div class="hero-actions"><a class="btn btn-primary" href="#">Book Now</a><a class="btn btn-outline" href="#">Pay for a Trip</a></div>
</div>
<div class="abs slider-dots"><span></span><span></span><span></span></div>

<div class="abs about-frame"></div>
<div class="abs about-photo" role="img" aria-label="Aerial view of a palm-fringed coastal village"></div>
<div class="abs about-copy">
  <p class="eyebrow">About Us</p>
  <h2 class="about-title">DRIFT US TO HAVEN</h2>
  <div class="rule"></div>
  <p class="about-text">Nemo enim ipsam voluptatem quia voluptas sit aspernatur aut odit aut fugit, sed quia consequuntur magni dolores eos qui ratione voluptatem sequi nesciunt. Neque porro quisquam est, qui dolorem ipsum quia dolor sit amet, consectetur, adipisci velit, sed quia non numquam eius modi tempora incidunt ut labore et dolore magnam aliquam quaerat voluptatem.</p>
  <a class="btn btn-primary about-btn" href="#">Read More</a>
</div>

<section class="abs band-grey" style="top:1340px;height:651px"></section>
<h2 class="abs section-title" style="top:1405px">Our Deluxe Tours Are</h2>
<div class="abs tour tour-main" role="img" aria-label="Singapore waterfront at dusk"><span class="tour-label">SINGAPORE</span></div>
<div class="abs tour t1" role="img" aria-label="Coastal city skyline beside turquoise water"></div>
<div class="abs tour t2" role="img" aria-label="City skyline lit at sunset"></div>
<div class="abs tour t3" role="img" aria-label="Harbour with a red-sailed junk boat"></div>
<div class="abs tour t4" role="img" aria-label="Colourful park overlooking a city"></div>
<div class="abs carousel-dots"><span></span><span></span><span></span></div>

<h2 class="abs section-title" style="top:2090px">Documentaries</h2>
<a class="abs video v1" href="#" role="img" aria-label="Documentary video still of travellers">
  <svg width="72" height="72" viewBox="0 0 72 72"><circle cx="36" cy="36" r="33" fill="none" stroke="#fff" stroke-width="3"/><path d="M28 22 L52 36 L28 50 Z" fill="none" stroke="#fff" stroke-width="3" stroke-linejoin="round"/></svg>
</a>
<a class="abs video v2" href="#" role="img" aria-label="Documentary video still of a garden path">
  <svg width="72" height="72" viewBox="0 0 72 72"><circle cx="36" cy="36" r="33" fill="none" stroke="#fff" stroke-width="3"/><path d="M28 22 L52 36 L28 50 Z" fill="none" stroke="#fff" stroke-width="3" stroke-linejoin="round"/></svg>
</a>
<p class="abs video-caption" style="left:118px;top:2572px;width:468px">Radiant Isles</p>
<p class="abs video-caption" style="left:609px;top:2562px;width:465px">Film Production Company<br>Greenharbour Films.</p>

<section class="abs band-grey" style="top:2742px;height:550px"></section>
<h2 class="abs section-title" style="top:2812px">Our Experts</h2>
<div class="abs arrow-btn" style="left:52px;top:3026px"><svg width="16" height="16" viewBox="0 0 16 16"><path d="M10 2 L4 8 L10 14" fill="none" stroke="#222" stroke-width="2"/></svg></div>
<div class="abs arrow-btn" style="left:1094px;top:3026px"><svg width="16" height="16" viewBox="0 0 16 16"><path d="M6 2 L12 8 L6 14" fill="none" stroke="#222" stroke-width="2"/></svg></div>
<div class="abs expert" style="left:112px;top:2955px"><div class="avatar" role="img" aria-label="Portrait of Sekar Pellow"></div><p class="expert-name">Sekar Pellow</p></div>
<div class="abs expert" style="left:363px;top:2955px"><div class="avatar" role="img" aria-label="Portrait of Garrick Pellow"></div><p class="expert-name">Garrick Pellow</p></div>
<div class="abs expert-card">
  <svg width="256" height="120" viewBox="0 0 256 120"><path d="M0 0 H256 V120 Q128 30 0 120 Z" fill="#0792cd"/></svg>
  <div class="avatar" role="img" aria-label="Portrait of Marcus Thornbury"></div>
  <p class="expert-name">Marcus Thornbury</p>
  <p class="expert-email">mthornbury17@mailbay.example</p>
</div>
<div class="abs expert" style="left:863px;top:2955px"><div class="avatar" role="img" aria-label="Portrait of Ratna Wulansari"></div><p class="expert-name">Ratna Wulansari</p></div>

<footer class="abs site-footer"></footer>
<div class="abs footer-brand"><span class="brand-mark"></span><span class="brand-name">Drift Us to Haven</span></div>
<div class="abs" style="left:493px;top:3348px;width:290px">
  <h3 class="footer-heading">Sign Up For Newsletter</h3>
  <p class="footer-text" style="margin-top:18px">excepteur sint occaecat cupidatat non proident, sunt in culpa qui officia</p>
  <div class="field" style="margin-top:16px">Enter email</div>
  <div class="subscribe" style="margin-top:16px">Subscribe</div>
</div>
<div class="abs" style="left:825px;top:3348px;width:330px">
  <h3 class="footer-heading" style="margin-bottom:22px">Contact Us</h3>
  <div class="contact-row"><svg width="14" height="18" viewBox="0 0 14 18"><path d="M7 0 C3 0 0 3 0 7 C0 12 7 18 7 18 C7 18 14 12 14 7 C14 3 11 0 7 0 Z M7 9.5 A2.5 2.5 0 1 1 7 4.5 A2.5 2.5 0 1 1 7 9.5 Z" fill="#fff"/></svg><p class="footer-text">27 Harlow rd Kestrel vale<br>Perth, Western Australia 6155</p></div>
  <div class="contact-row"><svg width="14" height="16" viewBox="0 0 14 16"><path d="M3 0 L6 4 L4 6 C5 9 7 11 10 12 L12 10 L14 13 L11 16 C5 15 0 9 0 3 Z" fill="#fff"/></svg><p class="footer-text">Phone:<br>(08) 9000 4127</p></div>
  <div class="contact-row"><svg width="16" height="12" viewBox="0 0 16 12"><rect width="16" height="12" fill="#fff"/><path d="M0 0 L8 7 L16 0" fill="none" stroke="#1f1f21" stroke-width="1.5"/></svg><p class="footer-text">Email:<br>driftustohavennz@mailbay.example</p></div>
</div>
<div class="abs socials"><span></span><span></span><span></span><span></span></div>
<p class="abs copyright">© 2019 All Rights Reserved | Privacy Policy | Terms and Conditions</p>

</body>
</html>
```